Design a 1-page brochure with our "The Harbinger Pathway" illustrated.

i have included my logo, an outline of the text and name of each step, and a quick sketch of generally how i would like the image to look. But please make it look sexy.

Each step should include the subtext as shown on the pdf attached. i.e. The first part of the image (far left) is "Problems", under that should list : 1. Poor Expectations; 2. Poor Communication... and so on for all the steps included.

I have also included a previous brochure that shows our branding and style.

Target Market(s)

Restaurant, Retail, Commercial

Industry/Entity Type

Construction Management

Font styles to use
Sans Serif

Colors
EB3D1F
EC4F4E
F09395
F8D3D4
FCEDEE

Requirements
Must have
• Our logo. Title of graphic: The Harbinger Pathway, our website and IG. www.quorvanbuildco.example. @quorvanbuildco

```html
<!DOCTYPE html>
<html lang="en">
<head>
<meta charset="utf-8">
<title>The Harbinger Pathway</title>
<link rel="stylesheet" href="https://fonts.googleapis.com/css2?family=Open+Sans:wght@400;600;700;800&display=swap">
<style>
  :root {
    --red: #eb3d1f;
    --red-deep: #9b1b22;
    --red-soft: #ec4f4e;
    --ink: #111111;
    --charcoal: #2a2a2a;
    --grey-hex: #a9abae;
    --paper: #ffffff;
    --mist: #f1f1f2;
    --text-light: #ffffff;
  }
  * { box-sizing: border-box; margin: 0; padding: 0; }
  html, body {
    width: 1200px; height: 936px; overflow: hidden;
    background: var(--paper);
    font-family: "Open Sans", Arial, sans-serif;
  }
  .brochure {
    position: relative; width: 1200px; height: 936px; overflow: hidden;
    background:
      linear-gradient(180deg, rgba(255,255,255,0) 60%, var(--paper) 92%),
      linear-gradient(135deg, var(--mist) 0%, var(--paper) 35%, var(--mist) 60%, var(--paper) 85%);
  }
  .shapes { position: absolute; inset: 0; }
  .brand {
    position: absolute; top: 80px; left: 0; width: 100%;
    display: flex; flex-direction: column; align-items: center; gap: 22px;
  }
  .brand__square { width: 70px; height: 70px; background: var(--red); }
  .brand__name {
    font-weight: 800; font-size: 13px; letter-spacing: 0.6px;
    color: var(--ink); text-transform: uppercase;
  }
  .title {
    position: absolute; top: 238px; left: 0; width: 100%;
    text-align: center; font-weight: 800; font-size: 55px;
    color: var(--ink); text-transform: uppercase; letter-spacing: 0.5px;
  }
  .wordmark {
    position: absolute; left: 44px; top: 418px; width: 190px;
    font-weight: 800; font-size: 34px; line-height: 1.05;
    color: var(--red); text-transform: uppercase;
  }
  .step {
    position: absolute; width: 160px; color: var(--text-light);
  }
  .step--top { top: 420px; }
  .step--bottom { top: 623px; }
  .step__name {
    text-align: center; font-weight: 700; font-size: 16px;
    text-transform: uppercase; margin-bottom: 9px;
  }
  .step__list {
    list-style: none; font-size: 10.5px; line-height: 1.3; font-weight: 600;
  }
  .step__list li { padding-left: 9px; position: relative; }
  .step__list li::before { content: "•"; position: absolute; left: 0; }
  .step--small .step__name { margin-bottom: 5px; }
  .step--small .step__list { font-size: 8.2px; line-height: 1.18; }
  .web {
    position: absolute; top: 851px; left: 0; width: 100%;
    display: flex; justify-content: center; align-items: center; gap: 12px;
    font-weight: 700; font-size: 21px; color: var(--ink);
  }
  .web svg { width: 20px; height: 20px; }
</style>
</head>
<body>
<main class="brochure">
  <svg class="shapes" viewBox="0 0 1200 936" width="1200" height="936">
    <defs>
      <radialGradient id="darkHex" cx="50%" cy="70%" r="70%">
        <stop offset="0" stop-color="#4a4a4a"/>
        <stop offset="1" stop-color="#0d0d0d"/>
      </radialGradient>
      <linearGradient id="redHex" x1="0" y1="0" x2="1" y2="1">
        <stop offset="0" stop-color="#ef3a2c"/>
        <stop offset="0.55" stop-color="#d42a26"/>
        <stop offset="1" stop-color="#8e1a1f"/>
      </linearGradient>
      <linearGradient id="band" x1="0" y1="0" x2="1" y2="0">
        <stop offset="0" stop-color="#e23127"/>
        <stop offset="0.6" stop-color="#c3222a"/>
        <stop offset="1" stop-color="#3a0c10"/>
      </linearGradient>
    </defs>

    <g class="hex-dark" fill="url(#darkHex)">
      <polygon points="439,367 537,418 537,520 439,571 341,520 341,418"/>
      <polygon points="754,367 852,418 852,520 754,571 656,520 656,418"/>
      <polygon points="1069,367 1167,418 1167,520 1069,571 971,520 971,418"/>
    </g>
    <g class="hex-red" fill="url(#redHex)">
      <polygon points="291,561 389,612 389,714 291,765 193,714 193,612"/>
      <polygon points="601,561 699,612 699,714 601,765 503,714 503,612"/>
      <polygon points="911,561 1009,612 1009,714 911,765 813,714 813,612"/>
    </g>
    <g class="hex-icon" fill="var(--grey-hex)" stroke="#ffffff" stroke-width="3">
      <polygon role="img" aria-label="Icon: builder in hard hat with tools" points="293,520 335,543 335,589 293,612 251,589 251,543"/>
      <polygon role="img" aria-label="Icon: rising bar chart with arrow" points="446,603 488,626 488,672 446,695 404,672 404,626"/>
      <polygon role="img" aria-label="Icon: pencil and ruler" points="601,520 643,543 643,589 601,612 559,589 559,543"/>
      <polygon role="img" aria-label="Icon: monitor showing charts" points="755,603 797,626 797,672 755,695 713,672 713,626"/>
      <polygon role="img" aria-label="Icon: builder with clipboard" points="913,520 955,543 955,589 913,612 871,589 871,543"/>
      <polygon role="img" aria-label="Icon: gears" points="1075,603 1117,626 1117,672 1075,695 1033,672 1033,626"/>
    </g>

    <g class="footer-band">
      <rect x="0" y="896" width="1200" height="22" fill="url(#band)"/>
      <polygon points="140,896 300,896 280,918 120,918" fill="#f05a4a" opacity="0.55"/>
      <polygon points="520,896 700,896 680,918 500,918" fill="#ffffff" opacity="0.12"/>
      <polygon points="860,896 1000,896 980,918 840,918" fill="#000000" opacity="0.2"/>
    </g>
  </svg>

  <header class="brand">
    <div class="brand__square"></div>
    <div class="brand__name">Quorvan Build Co</div>
  </header>

  <h1 class="title">The Harbinger Pathway</h1>

  <div class="wordmark">Quorvan<br>Build<br>Co</div>

  <section class="step step--top" style="left:359px;">
    <h2 class="step__name">Organize</h2>
    <ul class="step__list">
      <li>Develop Project Plan</li>
      <li>Develop Schedule</li>
      <li>Develop Budget</li>
    </ul>
  </section>

  <section class="step step--top" style="left:667px; width:176px;">
    <h2 class="step__name">Manage</h2>
    <ul class="step__list">
      <li>O.O.D.A</li>
      <li>Shared Consciousness Meetings</li>
      <li>Pressurized Collaboration</li>
    </ul>
  </section>

  <section class="step step--top step--small" style="left:990px; width:160px;">
    <h2 class="step__name">Possibility</h2>
    <ul class="step__list">
      <li>Project Synergy</li>
      <li>Excellent Communication where Budget and Schedule are visible and approved.</li>
      <li>Clear project visibility where everyone understands how we got to a successful end.</li>
      <li>Everyone involved is proud of the final product.</li>
    </ul>
  </section>

  <section class="step step--bottom" style="left:203px; width:180px;">
    <h2 class="step__name">Common Problems</h2>
    <ul class="step__list">
      <li>Changing or poor expectations.</li>
      <li>Poor Communication</li>
      <li>No Journey To Success</li>
      <li>No Trust</li>
      <li>No Accountability</li>
    </ul>
  </section>

  <section class="step step--bottom" style="left:521px;">
    <h2 class="step__name">Execute</h2>
    <ul class="step__list">
      <li>Project Start</li>
    </ul>
  </section>

  <section class="step step--bottom" style="left:831px;">
    <h2 class="step__name">Complete</h2>
    <ul class="step__list">
      <li>Project Closeout</li>
    </ul>
  </section>

  <footer class="web">
    <svg viewBox="0 0 20 20" aria-hidden="true" fill="none" stroke="#111" stroke-width="1.6">
      <circle cx="10" cy="10" r="8.5"/>
      <ellipse cx="10" cy="10" rx="3.8" ry="8.5"/>
      <line x1="1.5" y1="10" x2="18.5" y2="10"/>
      <line x1="3" y1="5.5" x2="17" y2="5.5"/>
      <line x1="3" y1="14.5" x2="17" y2="14.5"/>
    </svg>
    <span>www.quorvanbuildco.example</span>
  </footer>
</main>
</body>
</html>
```